AWESOME RETAILER OF PHONE ACCESSORIES NEEDS AWESOME WEBSITE FROM AWESOME DESIGNER

We currently do not have any website and are looking for one for our new store. We are a retailer who sells novaphone accessories, speakers, electronics, cables with the best pricing guaranteed. We carry all top name brands including:

TrailGuard : http://www.trailguard-cases.example/en/

Ferncase : http://www.ferncase.example/

Quindle : http://www.quindle.example/Default.asp

Varenta : http://www.varenta.example/

Bold Kit : http://www.bold-kit.example/

http://www.glintshield.example/hot-sellers/handset-5-frost-white.html

http://www.tamsel-works.example/products/detail.cfm?prodID=2

http://vostrek.example/

http://www.plimm.example/

We would like to see our logo's used and a website that is trendy and catchy to our demographics. Our demographic is male/female between the ages of 16-45.

Target Market(s)

Male/Femal Ages -16-45

Industry/Entity Type

Electronics

Requirements
Must have
• Must use our logo's and be a catchy fun website keeps the customers eye.
Coupon Tab where customers can print coupons
Products Tab where we can display all of our brands of products
Contact us page
Location Page
CHATTERLY/BLURTLY ACCOUNT TO BE LINKED TO SITE
WEBSITE WILL BE HOSTED BY HOSTWREN.EXAMPLE PLEASE MAKE SURE YOUR DESIGN IS COMPATIBLE WITH THEM.

PLEASE BE SURE TO USE OUR LOGO IN YOUR DESIGN YOU SUBMIT, THEY ARE ATTACHED TO THIS PROJECT
Nice to have
• We would like a slot where a video can be posted from clipvane
Authorized dealer banner
Should not have
• not a dark website but bright and vibrant
Do not use any logos or images that are trademarked by Quorral.

```html
<!DOCTYPE html>
<html lang="en">
<head>
<meta charset="utf-8">
<title>Kellvo — Phone Accessories</title>
<link rel="stylesheet" href="https://fonts.googleapis.com/css2?family=Oswald:wght@400;500&family=Open+Sans:wght@400;600;700&display=swap">
<style>
:root{
  --green:#9cc92d;
  --green-dark:#7fae1c;
  --logo-green:#6aa51f;
  --accent-green:#8dc63f;
  --ink:#222;
  --grey:#8a8a8a;
  --line:#cfcfcf;
  --band:rgba(40,40,40,.88);
  --white:#fff;
  --nav-active:#4a4a4a;
}
*{box-sizing:border-box;margin:0;padding:0}
html,body{width:895px;height:1200px;overflow:hidden;background:var(--white)}
body{position:relative;font-family:"Open Sans",Arial,sans-serif;color:var(--ink)}
.abs{position:absolute}

/* header */
.brand{left:137px;top:14px;display:flex;align-items:center;gap:10px}
.brand-mark{width:30px;height:30px;background:var(--logo-green)}
.brand-name{font-family:"Open Sans",sans-serif;font-weight:600;font-size:40px;line-height:1;color:var(--logo-green)}

.navbar{left:0;top:95px;width:895px;height:30px;background:linear-gradient(var(--green),var(--green-dark))}
.nav{left:83px;top:0;display:flex;height:30px}
.nav a{display:block;height:30px;line-height:30px;padding:0 9px;border-left:1px solid #3f5a10;font-family:"Oswald",sans-serif;font-size:13px;color:var(--white);text-decoration:none;text-transform:uppercase}
.nav a:last-child{border-right:1px solid #3f5a10}
.nav a.active{background:var(--nav-active)}
.search-field{left:648px;top:4px;width:118px;height:22px;border-radius:11px;background:var(--white);font-size:11px;line-height:22px;padding-left:12px;color:#555}
.search-btn{left:772px;top:5px;width:58px;height:20px;background:#b9b9b9;border:1px solid #888;font-family:"Oswald",sans-serif;font-size:11px;line-height:18px;text-align:center;color:var(--white)}

/* slider */
.slider{left:81px;top:128px;width:750px;height:321px;background:var(--white)}
.slide-title{left:40px;top:14px;font-family:Arial,sans-serif;font-size:76px;font-weight:400;color:var(--accent-green);letter-spacing:1px;line-height:1}
.slide-desc{left:47px;top:150px;width:360px;font-size:14px;line-height:20px;color:var(--grey)}
.slide-image{left:434px;top:100px;width:286px;height:136px}
.arrow{width:32px;height:32px}
.arrow-prev{left:11px;top:112px}
.arrow-next{left:703px;top:112px}
.caption{left:0;top:239px;width:750px;height:82px;background:var(--band);color:var(--white);padding:12px 12px}
.caption h2{font-size:15px;font-weight:700;margin-bottom:10px}
.caption p{font-size:11px;line-height:16px;font-weight:600}

/* side boxes */
.box{border:1px solid var(--line);background:var(--white)}
.box-head{height:24px;background:var(--green);font-family:"Oswald",sans-serif;font-size:12px;line-height:24px;color:var(--white);padding-left:10px;text-transform:uppercase}
.latest{left:81px;top:473px;width:169px;height:215px}
.product-image{left:0;top:38px;width:167px;height:106px}
.product-caption{left:0;top:144px;width:167px;height:52px;background:var(--band);color:var(--white);font-weight:700;font-size:14px;padding:14px 16px}

/* video */
.video{left:273px;top:473px;width:383px;height:274px;background:#111}
.video-frame{left:0;top:8px;width:383px;height:225px}
.video-controls{left:0;top:233px;width:383px;height:41px;background:#1a1a1a;color:var(--white);font-size:16px}

/* login */
.login{left:659px;top:473px;width:171px;height:265px}
.login label{display:block;font-size:9px;color:#333}
.field{width:138px;height:22px;border:1px solid #b9b9b9;border-radius:3px;font-size:9px;line-height:20px;padding-left:20px;color:#999;position:relative}
.field svg{position:absolute;left:6px;top:5px}
.login-btn{width:50px;height:20px;background:#a5a5a5;color:var(--white);font-family:"Oswald",sans-serif;font-size:11px;line-height:20px;text-align:center}
.login-links{list-style:none;font-size:11px;color:#1a6fb0}
.login-links li{display:flex;align-items:center;gap:8px;margin-bottom:4px}

/* article */
.article{left:273px;top:766px;width:383px;font-size:11px;line-height:16px;color:#333}

.tagline{left:0;top:1062px;width:895px;text-align:center;font-family:"Open Sans",sans-serif;font-weight:400;font-size:32px;color:#111;letter-spacing:-.5px}
.tagline em{font-style:normal;color:var(--accent-green)}

/* footer */
.footer{left:0;top:1122px;width:895px;height:78px;background:var(--green)}
.social{left:83px;top:18px;display:flex;gap:7px}
.social span{display:block;height:28px;padding:0 4px;font-size:8px;font-weight:700;line-height:28px;color:var(--white);background:#4e7d14}
.social span.plain{width:28px;padding:0}
.copyright{left:81px;top:64px;font-size:7px;color:var(--white)}
.credit{right:80px;top:64px;font-size:7px;color:#333}
</style>
</head>
<body>

<header>
  <div class="abs brand"><span class="brand-mark"></span><span class="brand-name">Kellvo</span></div>
  <nav class="abs navbar">
    <div class="abs nav">
      <a class="active">Home</a><a>Products</a><a>About Us</a><a>Sign Up</a><a>Contact Us</a><a>Repair</a>
    </div>
    <div class="abs search-field">Search...</div>
    <div class="abs search-btn">SEARCH</div>
  </nav>
</header>

<section class="abs slider">
  <h1 class="abs slide-title">accessories</h1>
  <p class="abs slide-desc">Description about cables which sell by Kellvo.Description about cables which sell by Kellvo.Description about cables which sell by Kellvo.</p>
  <svg class="abs slide-image" role="img" aria-label="Three colourful phone cases in yellow, magenta and black" viewBox="0 0 286 136" preserveAspectRatio="none">
    <defs><linearGradient id="cases" x1="0" x2="1"><stop offset="0" stop-color="#e8c020"/><stop offset=".5" stop-color="#b1208f"/><stop offset="1" stop-color="#2a2a2a"/></linearGradient></defs>
    <rect width="286" height="136" rx="12" fill="url(#cases)" opacity=".85"/>
  </svg>
  <svg class="abs arrow arrow-prev" viewBox="0 0 32 32"><circle cx="16" cy="16" r="15" fill="#777"/><path d="M19 9l-7 7 7 7" stroke="#fff" stroke-width="3" fill="none"/></svg>
  <svg class="abs arrow arrow-next" viewBox="0 0 32 32"><circle cx="16" cy="16" r="15" fill="#777"/><path d="M13 9l7 7-7 7" stroke="#fff" stroke-width="3" fill="none"/></svg>
  <div class="abs caption">
    <h2>Accessories</h2>
    <p>Pellentesque habitant morbi tristique senectus et netus et malesuada fames ac turpis egestas. In posuere felis nec tortor. Pellentesque faucibus.</p>
  </div>
</section>

<aside class="abs box latest">
  <div class="box-head">Latest Products</div>
  <svg class="abs product-image" role="img" aria-label="Portable speaker product photo" viewBox="0 0 167 106">
    <rect width="167" height="106" fill="#cfcfcf"/>
    <circle cx="22" cy="34" r="10" fill="#666"/><path d="M25 28l-6 6 6 6" stroke="#fff" stroke-width="2" fill="none"/>
    <circle cx="139" cy="34" r="10" fill="#666"/><path d="M136 28l6 6-6 6" stroke="#fff" stroke-width="2" fill="none"/>
  </svg>
  <div class="abs product-caption">Product 4</div>
</aside>

<section class="abs video">
  <svg class="abs video-frame" role="img" aria-label="Video still of a phone on a desk" viewBox="0 0 383 225">
    <defs><linearGradient id="still" x1="0" y1="0" x2="1" y2="1"><stop offset="0" stop-color="#6b5a4a"/><stop offset="1" stop-color="#2b2420"/></linearGradient></defs>
    <rect width="383" height="225" fill="url(#still)"/>
    <rect x="282" y="15" width="78" height="60" fill="#5a4a3e" opacity=".8"/>
    <rect x="282" y="85" width="78" height="60" fill="#5a4a3e" opacity=".8"/>
    <path d="M170 90v44l38-22z" fill="#fff"/>
  </svg>
  <div class="abs video-controls">
    <svg class="abs" style="left:14px;top:12px" width="16" height="18" viewBox="0 0 16 18"><path d="M0 0v18l16-9z" fill="#fff"/></svg>
    <span class="abs" style="left:60px;top:9px">01:14</span>
    <span class="abs" style="left:226px;top:9px">00:26</span>
    <svg class="abs" style="left:295px;top:12px" width="20" height="18" viewBox="0 0 20 18"><path d="M0 6h5l6-5v16l-6-5H0z" fill="#fff"/><path d="M14 5l5 8M19 5l-5 8" stroke="#fff" stroke-width="2"/></svg>
    <svg class="abs" style="left:348px;top:12px" width="18" height="18" viewBox="0 0 18 18" fill="none" stroke="#fff" stroke-width="2"><path d="M1 6V1h5M12 1h5v5M17 12v5h-5M6 17H1v-5"/></svg>
  </div>
</section>

<aside class="abs box login">
  <div class="box-head">Login</div>
  <div class="abs" style="left:6px;top:34px">
    <label>User Name</label>
    <div class="field" style="margin-top:5px"><svg width="9" height="10" viewBox="0 0 9 10"><circle cx="4.5" cy="3" r="2.5" fill="#888"/><path d="M0 10a4.5 4 0 019 0z" fill="#888"/></svg>User Name</div>
    <label style="margin-top:10px">Password</label>
    <div class="field" style="margin-top:5px"><svg width="9" height="10" viewBox="0 0 9 10"><rect y="4" width="9" height="6" fill="#888"/><path d="M2 4V3a2.5 2.5 0 015 0v1" stroke="#888" fill="none"/></svg>Password</div>
    <label style="margin-top:8px;display:flex;align-items:center;gap:4px"><span style="width:14px;height:14px;border:1px solid #777;display:inline-block"></span>Remember Me</label>
    <div class="login-btn" style="margin:2px 0 0 18px">LOG IN</div>
    <ul class="login-links" style="margin:12px 0 0 10px">
      <li><svg width="9" height="10" viewBox="0 0 9 10"><rect y="4" width="9" height="6" fill="#888"/><path d="M2 4V3a2.5 2.5 0 015 0v1" stroke="#888" fill="none"/></svg>Forgot your password?</li>
      <li><svg width="9" height="10" viewBox="0 0 9 10"><circle cx="4.5" cy="3" r="2.5" fill="#888"/><path d="M0 10a4.5 4 0 019 0z" fill="#888"/></svg>Forgot your username?</li>
      <li><svg width="9" height="10" viewBox="0 0 9 10"><rect x=".5" y=".5" width="8" height="9" fill="none" stroke="#888"/><path d="M2 5l2 2 4-5" stroke="#888" fill="none"/></svg>Create an account</li>
    </ul>
  </div>
</aside>

<article class="abs article">
  <p>Phasellus felis dolor, scelerisque a, tempus eget, lobortis id, libero. Donec scelerisque leo ac risus. Praesent sit amet est. In dictum, dolor eu dictum porttitor, enim felis viverra mi, eget luctus massa purus quis odio. Etiam nulla massa, pharetra facilisis, volutpat in, imperdiet sit amet, sem. Aliquam nec erat at purus cursus interdum. Vestibulum ligula augue, bibendum accumsan, vestibulum ut, commodo a, mi. Morbi ornare gravida elit. Integer congue, augue et malesuada iaculis, ipsum dui aliquet felis, at cursus magna nisl nec elit. Donec iaculis diam a nisi accumsan viverra. Duis sed tellus et tortor vestibulum gravida. Praesent elementum elit at tellus. Curabitur metus ipsum, luctus eu, malesuada ut, tincidunt sed, diam. Donec quis mi sed magna hendrerit accumsan. Suspendisse risus nibh, ultricies eu, volutpat non, condimentum hendrerit, augue. Etiam eleifend, metus vitae adipiscing semper, mauris ipsum iaculis elit, congue gravida elit mi egestas orci. Curabitur pede.</p>
</article>

<p class="abs tagline">SEE HOW PEOPLE LIVE IN <em>DIFFERENT</em> LIFE STYLE</p>

<footer class="abs footer">
  <div class="abs social">
    <span>CHATTERLY</span><span>BLURTLY</span><span>clipvane</span><span class="plain"></span>
  </div>
  <p class="abs copyright">Copyrights By Kellvo 2012</p>
  <p class="abs credit">Tessera 3.0 Templates by Brightnode Hosting</p>
</footer>

</body>
</html>
```